Silver Kettle Consulting

I need a business card design and for my consulting business. I provide outsourced CFO services for start-ups and high growth companies. I call my company Silver Kettle because building a company is similar to building a stone pathway, selecting each stone and planning several stones head in order to properly place them - all while keeping an eye on the final design and curve of the path. The underlying idea I want to express with my marketing images is that I'm someone that you can count on to help build your business and be there step by step to help. I'm not the old gray-haired CFO that many folks think of. :) I've included a one-page summery that I'm working on, it includes a summary of what I do. I've used a muted pathway and with greens in the header , and do like the green, but am open to other colors if they work well. Would like something that looks like a pathway, but a more abstract version instead of a picture.

Marketing

```html
<!DOCTYPE html>
<html lang="en">
<head>
<meta charset="utf-8">
<title>Silver Kettle Consulting – Business Card</title>
<link href="https://fonts.googleapis.com/css2?family=Open+Sans:wght@400;600;700&display=swap" rel="stylesheet">
<style>
  :root {
    --brand-green: #4a873f;
    --paper: #f6f7f6;
    --charcoal: #3a393b;
    --silver: #a9a6a7;
    --ink: #111111;
    --white: #ffffff;
  }
  * { margin: 0; padding: 0; box-sizing: border-box; }
  html, body {
    width: 999px; height: 1200px; overflow: hidden;
    background: var(--white);
    font-family: "Open Sans", Arial, sans-serif;
  }
  .card {
    position: absolute; left: 20px; width: 959px; height: 549px;
    box-shadow: 4px 5px 8px rgba(0,0,0,0.45);
    overflow: hidden;
  }
  .card--front { top: 28px; background: var(--paper); }
  .card--back { top: 615px; background: var(--brand-green); }
  .card__backdrop { position: absolute; inset: 0; width: 959px; height: 549px; }

  .brand { position: absolute; display: flex; align-items: center; }
  .brand__dot { border-radius: 50%; flex: none; }
  .brand__name { font-weight: 600; line-height: 0.98; }

  .card--front .brand { left: 27px; top: 298px; }
  .card--front .brand__dot { width: 104px; height: 104px; background: var(--brand-green); margin-right: 24px; }
  .card--front .brand__name { font-size: 52px; color: var(--brand-green); }

  .card--back .brand { left: 182px; top: 180px; }
  .card--back .brand__dot { width: 184px; height: 184px; background: var(--paper); margin-right: 20px; }
  .card--back .brand__name { font-size: 76px; color: var(--paper); line-height: 1.1; }

  .address {
    position: absolute; left: 34px; top: 450px;
    display: flex; align-items: flex-start; gap: 26px;
    font-size: 23px; line-height: 33px; color: var(--ink);
  }
  .address__pin { width: 24px; height: 42px; margin-top: 10px; }

  .person { position: absolute; left: 562px; top: 316px; color: var(--ink); }
  .person__name { font-size: 40px; font-weight: 700; line-height: 1.1; }
  .person__role { font-size: 27px; line-height: 1.1; margin-top: 2px; }

  .contacts { position: absolute; left: 561px; top: 412px; list-style: none; }
  .contacts__item {
    display: flex; align-items: center; height: 33px;
    font-size: 24px; color: var(--ink);
  }
  .contacts__icon { width: 26px; height: 26px; margin-right: 26px; }
</style>
</head>
<body>

<section class="card card--front" aria-label="Business card front">
  <svg class="card__backdrop" viewBox="0 0 959 549" aria-hidden="true">
    <rect width="959" height="549" fill="var(--brand-green)"/>
    <path d="M0,227 C200,128 330,118 430,118 C650,125 860,180 959,228 L959,549 L0,549Z" fill="var(--silver)"/>
    <path d="M430,126 C650,134 860,190 959,238 L959,320 C850,240 650,150 430,126Z" fill="var(--charcoal)"/>
    <path d="M0,236 C200,140 330,128 430,126 C650,150 850,240 959,320 L959,549 L0,549Z" fill="var(--paper)"/>
  </svg>

  <div class="brand">
    <span class="brand__dot"></span>
    <span class="brand__name">Silver<br>Kettle</span>
  </div>

  <div class="address">
    <svg class="address__pin" viewBox="0 0 24 42" aria-hidden="true">
      <path d="M12,0 C5,0 0,5 0,12 C0,21 12,42 12,42 C12,42 24,21 24,12 C24,5 19,0 12,0Z" fill="var(--ink)"/>
      <circle cx="12" cy="12" r="5" fill="var(--paper)"/>
    </svg>
    <p>suit # 00, Lorem ipsum<br>Lorem Lorem ipsum</p>
  </div>

  <div class="person">
    <h1 class="person__name">Name Title</h1>
    <p class="person__role">designation</p>
  </div>

  <ul class="contacts">
    <li class="contacts__item">
      <svg class="contacts__icon" viewBox="0 0 26 26" aria-hidden="true">
        <path d="M6,2 L10,2 L12,8 L9,10 C10,13 13,16 16,17 L18,14 L24,16 L24,20 C24,22 22,24 20,24 C10,23 3,16 2,6 C2,4 4,2 6,2Z" fill="none" stroke="var(--ink)" stroke-width="2.2"/>
        <path d="M15,3 A8,8 0 0 1 23,11 M15,7 A4,4 0 0 1 19,11" fill="none" stroke="var(--ink)" stroke-width="2"/>
      </svg>
      555-014-2368
    </li>
    <li class="contacts__item">
      <svg class="contacts__icon" viewBox="0 0 26 26" aria-hidden="true">
        <path d="M1,11 L13,2 L25,11 L25,24 L1,24Z" fill="var(--ink)"/>
        <path d="M4,13 L13,19 L22,13" fill="none" stroke="var(--paper)" stroke-width="2"/>
      </svg>
      dana@silverkettle.com
    </li>
    <li class="contacts__item">
      <svg class="contacts__icon" viewBox="0 0 26 26" aria-hidden="true">
        <g fill="none" stroke="var(--ink)" stroke-width="1.8">
          <circle cx="13" cy="13" r="11"/>
          <ellipse cx="13" cy="13" rx="5" ry="11"/>
          <path d="M2,13 L24,13 M4,7 L22,7 M4,19 L22,19 M13,2 L13,24"/>
        </g>
      </svg>
      www.silverkettle.com
    </li>
  </ul>
</section>

<section class="card card--back" aria-label="Business card back">
  <div class="brand">
    <span class="brand__dot"></span>
    <span class="brand__name">Silver<br>Kettle</span>
  </div>
</section>

</body>
</html>
```